"The Orignal LoopTabs" needs a Package Design!! Everybody's got a LoopTab, What's Yours?

I need eye popping packaging design!! My LoopTabs are gonna be big! I'm a single mom I'm based in AZ, so this is big for me. The LoopTabs keep towels off the floor & so much more!! Color cardboard insert background, bright yellow and Bright blue, like a caribbean blue, funky font for the Product Name. The Original, can be smaller and in an easy script. I have some pictures so you can get an concept and basic design ideas. There are no limits to their uses!! Please call me for any questions or direction.
Updates

I want to thank you all for participating, You each brought a different perspective and had some really good ideas. I will definitely us this service again! Thank you, Dolores Fitchley

Target Market(s)

Mom's, woman, men, students you name it!!

Colors
fbee3e
0293ce

Requirements
Must have
• Clear pvc packaging so you can see the product and they have to hang over so you see how they are used. The look needs to draw people in to it!! Read my instructions on the downloaded pics and info and if you have questions please let me know. The towel and towel bar can be like a drawing not actual towel picture. On the reverse side is a list of ideas and my website. Other colors for lettering aside from the Caribbean blue for the word "LoopTabs" is up to you, use your expertise.
Should not have
• The blue is not on the color wheel that is shown here.

```html
<!DOCTYPE html>
<html lang="en">
<head>
<meta charset="utf-8">
<title>The Orignal LoopTabs – Package Card</title>
<link href="https://fonts.googleapis.com/css2?family=Titan+One&family=Bangers&family=Arimo:wght@400;700&family=Nunito:wght@800&display=swap" rel="stylesheet">
<style>
  :root {
    --yellow: #fbee3e;
    --yellow-glow: #fdf7a8;
    --blue: #0293ce;
    --blue-deep: #1a86c7;
    --red: #e0202a;
    --white: #ffffff;
    --backdrop: #9a6a3c;
    --pink: #e8337a;
    --lime: #8fd23a;
  }
  * { box-sizing: border-box; margin: 0; padding: 0; }
  html, body { width: 1200px; height: 796px; overflow: hidden; }
  body { background: var(--backdrop); position: relative; font-family: "Arimo", Arial, sans-serif; }

  .card {
    position: absolute;
    background: radial-gradient(ellipse at 50% 55%, var(--yellow-glow) 0%, var(--yellow) 60%);
    box-shadow: 0 2px 6px rgba(0,0,0,.35);
  }

  /* ---------- Front card ---------- */
  .front { left: 28px; top: 107px; width: 555px; height: 666px; }
  .brand-name {
    position: absolute; left: 0; right: 0; top: 42px;
    text-align: center; font-family: "Arimo", Arial, sans-serif; font-weight: 700;
    color: var(--blue); font-size: 48px; line-height: 54px;
  }

  .tagline-band {
    position: absolute; left: 0; right: 0; top: 163px; height: 70px;
    background: var(--blue); border-top: 4px solid var(--white);
    color: var(--white); text-align: center; font-size: 19px; line-height: 27px; padding-top: 8px;
  }

  .product-window {
    position: absolute; left: 76px; top: 258px; width: 416px; height: 195px;
    background: var(--blue); border-radius: 10px; padding: 12px 14px;
    box-shadow: 0 0 8px rgba(255,255,255,.7);
  }
  .product-photo {
    width: 100%; height: 100%;
    background: linear-gradient(90deg, var(--pink) 0%, #c81e4c 22%, #f2f2f2 30%, var(--pink) 48%, #c81e4c 60%, #2a8fc8 72%, var(--lime) 82%, #c9c9c9 100%);
  }

  .slogan-box {
    position: absolute; left: 40px; top: 478px; width: 475px; height: 105px;
    background: var(--blue); border: 4px solid var(--white);
    box-shadow: 0 2px 4px rgba(0,0,0,.25);
    font-family: "Bangers", sans-serif; color: var(--white); font-size: 36px; letter-spacing: 1px;
    text-align: center; line-height: 40px; padding-top: 10px;
  }
  .count-badge {
    position: absolute; left: 452px; top: 534px; width: 84px; height: 84px; border-radius: 50%;
    background: var(--blue); border: 4px solid var(--white);
    color: var(--white); font-weight: 700; font-size: 9.5px; text-align: center;
    display: flex; flex-direction: column; justify-content: center; line-height: 15px;
  }
  .pack-note { position: absolute; left: 0; width: 535px; top: 598px; text-align: center; color: var(--red); font-size: 13px; font-weight: 700; }

  /* ---------- Back card ---------- */
  .back { left: 623px; top: 30px; width: 552px; height: 663px; }
  .back-heading {
    position: absolute; left: 0; right: 0; top: 60px; text-align: center;
    font-family: "Titan One", sans-serif; color: var(--blue); font-size: 14px; line-height: 22px; letter-spacing: .5px;
  }
  .back-heading .accent { color: var(--red); font-size: 19px; }
  .back-heading .accent-small { color: var(--red); }
  .uses-gallery { position: absolute; left: 37px; top: 138px; display: flex; gap: 12px; }
  .use-thumb {
    width: 112px; height: 127px; background: var(--blue); border-radius: 10px; padding: 8px;
    box-shadow: 0 2px 3px rgba(0,0,0,.3);
  }
  .use-thumb span { display: block; width: 100%; height: 100%; border-radius: 3px; }
  .thumb-bib span { background: linear-gradient(180deg, #c9a48a, #7ab8de); }
  .thumb-towel span { background: linear-gradient(180deg, #ffffff, #b3263a 70%, #ffffff); }
  .thumb-wrap span { background: linear-gradient(180deg, #f3f3f3, #c6e08a 60%, #f3f3f3); }
  .thumb-shade span { background: linear-gradient(180deg, #8b6f5a 35%, #cfe0ec 40%, #9cc4e4); }

  .uses-list {
    position: absolute; top: 279px; list-style: none;
    font-family: "Nunito", sans-serif; color: var(--blue-deep); font-size: 15.5px; font-weight: 800;
  }
  .uses-list li { position: relative; height: 21.6px; line-height: 21.6px; padding-left: 20px; white-space: nowrap; }
  .uses-list li::before {
    content: "✓"; position: absolute; left: 0; top: 4px; width: 13px; height: 13px;
    background: var(--blue); border-radius: 2px; color: var(--white); font-size: 11px; line-height: 13px; text-align: center;
  }
  .uses-list.left { left: 58px; }
  .uses-list.right { left: 282px; top: 277px; }

  .back-closing { position: absolute; left: 0; right: 0; top: 553px; text-align: center; font-family: "Titan One", sans-serif; color: var(--red); font-size: 20px; letter-spacing: 1px; }
  .back-site { position: absolute; left: 0; right: 0; top: 587px; text-align: center; color: var(--red); font-weight: 700; font-size: 13px; }
</style>
</head>
<body>

<section class="card front" aria-label="Package front">
  <h1 class="brand-name">The Orignal<br>LoopTabs</h1>
  <div class="tagline-band">NO MORE TOWELS ON THE FLOOR<br>&amp; SO MUCH MORE!!!</div>
  <div class="product-window">
    <div class="product-photo" role="img" aria-label="Four LoopTab clips in red, white, red and silver on colorful ribbon straps"></div>
  </div>
  <div class="slogan-box">EVERYBODY'S GOT A LOOPTAB<br>WHAT'S YOURS?</div>
  <div class="count-badge"><span>4 LOOPTABS</span><span>per box</span></div>
  <p class="pack-note">Thin clear rubber band to hold product in place.</p>
</section>

<section class="card back" aria-label="Package back">
  <div class="back-heading">
    <span class="accent">ENDLESS USES</span> – POST A PICTURE OF YOUR<br>
    LOOPTAB IDEA TO OUR WEBSITE AND YOU COULD WIN<br>
    A <span class="accent">FREE</span> PACKAGE OF <span class="accent-small">LIMITED EDITION LOOPTABS'</span>!!
  </div>
  <div class="uses-gallery">
    <div class="use-thumb thumb-bib"><span role="img" aria-label="Toddler wearing a towel clipped as a bib"></span></div>
    <div class="use-thumb thumb-towel"><span role="img" aria-label="Red towel hanging from a towel bar by a clip"></span></div>
    <div class="use-thumb thumb-wrap"><span role="img" aria-label="Green towel clipped as a body wrap"></span></div>
    <div class="use-thumb thumb-shade"><span role="img" aria-label="Clip used as a pull-down for a window shade"></span></div>
  </div>
  <ul class="uses-list left">
    <li>Baby Bibs</li><li>Baby Strollers</li><li>Hanging Bathing Suits</li><li>By the Pool</li>
    <li>Pull downs for Shades</li><li>Tarp Holders</li><li>Camping</li><li>Room Dividers</li>
    <li>College Dorms</li><li>The Gym</li><li>Photography Backdrops</li><li>Traveling</li>
  </ul>
  <ul class="uses-list right">
    <li>Towel wraps</li><li>Pet Training</li><li>Drying Lingerie</li><li>Tablecloths</li>
    <li>Dishtowels</li><li>The Garage</li><li>Hanging Quilts</li><li>To hold your pants closed</li>
    <li>Curtains (no sewing!)</li><li>Valences (no sewing!)</li><li>Drapes (no sewing!)</li><li>Shower Curtains</li>
  </ul>
  <p class="back-closing">THE ONLY LIMIT IS YOUR IMAGINATION</p>
  <p class="back-site">The original LoopTabs'.com</p>
</section>

</body>
</html>
```